Emergency Vehicle Installer and Security Firm Needs a Business Card

Our company "Corvalt" need a business card for our Emergency Vehicle Equipment Installation and Infrastructure Security Business. We are contract designers, manufacturers and installers for Emergency Vehicle Fleets. This includes installation of Emergency Lights, Sirens, Vehicle Graphics and Radio Communications. We also supply this products to an international market. We also do consultant, and installation of high level security access, alarm and surveillance equipment for medium to large size businesses.

The design should represent a level of trust in our professionalism and expertise. It should visually display our ongoing relationship with the emergency services, but not overtake our commitment to high level security options.

Target Market(s)

Emergency Services and Businesses requiring high level security

Industry/Entity Type

Business

Contact Information for Business Card

*note complete details will be given to the winning designer for revising. The name "Mark Pell will be used to fill in name".

Mark Pell
Managing Director
Corvalt NZ Limited
Phone: +64 027 604 91352
Email: mark.pell@corvalt-example.co.nz

Requirements
Must have
• Card must be in black. Using our logo on the top as supplied. Designers should try having the reverse side as a blurred image of police lights (red and blue) with our logo in greyscale in the centre (this is not particularly a requirement, but feel free to play around with this option).
Nice to have
• A card design that looks good when spot UV printed. A clean compact and graphic design. A grey scale feel on the front (excluding logo, but you can play around with that idea). Rounded smooth text.
Should not have
• Will update this section as designs come through - feel free to submit what you feel would look good.

```html
<!DOCTYPE html>
<html lang="en">
<head>
<meta charset="utf-8">
<title>Corvalt Business Card</title>
<link href="https://fonts.googleapis.com/css2?family=Roboto:wght@400;700&display=swap" rel="stylesheet">
<style>
  :root {
    --stage: #1c1c1e;
    --card-black: #050505;
    --brand-red: #e0231f;
    --brand-red-deep: #b8130f;
    --white: #ffffff;
    --soft-white: #e9e9e9;
    --logo-grey: #c9cbd0;
    --siren-blue: #1b3fd6;
    --siren-deep: #0b0f3d;
    --siren-red: #d5102a;
    --siren-violet: #5a1e7a;
  }
  * { box-sizing: border-box; margin: 0; padding: 0; }
  html, body {
    width: 1200px; height: 800px; overflow: hidden;
    background: var(--stage);
    font-family: "Roboto", Arial, sans-serif;
  }
  .canvas {
    position: relative; width: 1200px; height: 800px;
    display: flex; align-items: center; justify-content: center; gap: 40px;
  }
  .card {
    position: relative; width: 540px; height: 309px;
    border-radius: 6px; overflow: hidden;
    box-shadow: 0 10px 30px rgba(0,0,0,.5);
  }
  /* Front */
  .card-front { background: var(--card-black); color: var(--white); }
  .card-front .accent-curves { position: absolute; inset: 0; width: 100%; height: 100%; }
  .brand-name {
    position: absolute; left: 150px; top: 52px;
    font-weight: 700; font-size: 46px; letter-spacing: 2px;
    color: var(--white); text-transform: uppercase;
  }
  .contact-block { position: absolute; left: 186px; top: 162px; }
  .person-name {
    font-weight: 700; font-size: 17px; letter-spacing: 1px;
    text-transform: uppercase; margin-left: 16px; margin-bottom: 4px;
  }
  .role { font-size: 13px; margin-bottom: 4px; }
  .role .title { color: var(--brand-red); }
  .role .company { color: var(--white); }
  .contact-line {
    display: flex; align-items: center; gap: 6px;
    font-size: 12.5px; color: var(--soft-white); margin-bottom: 3px;
  }
  .contact-line svg { width: 11px; height: 11px; flex: none; }
  /* Back */
  .card-back { display: flex; align-items: center; justify-content: center; }
  .siren-glow {
    position: absolute; inset: 0;
    background:
      radial-gradient(ellipse 22% 20% at 55% 42%, rgba(255,255,255,.95), rgba(255,255,255,0) 70%),
      radial-gradient(ellipse 45% 55% at 20% 30%, var(--siren-blue), rgba(27,63,214,0) 70%),
      radial-gradient(ellipse 45% 55% at 85% 65%, var(--siren-red), rgba(213,16,42,0) 70%),
      linear-gradient(120deg, var(--siren-deep) 0%, var(--siren-blue) 35%, var(--siren-violet) 60%, var(--siren-red) 85%, #5a0a18 100%);
  }
  .card-back .brand-name {
    position: relative; left: auto; top: auto;
    color: var(--logo-grey); font-size: 58px;
  }
</style>
</head>
<body>
<main class="canvas">
  <section class="card card-front" aria-label="Card front">
    <svg class="accent-curves" viewBox="0 0 540 309" aria-hidden="true">
      <path d="M0 0 H70 Q20 150 60 309 H0 Z" fill="var(--brand-red)"/>
      <path d="M0 0 H40 Q5 150 30 309 H0 Z" fill="var(--brand-red-deep)"/>
      <path d="M540 120 Q430 180 460 309 H540 Z" fill="var(--white)"/>
    </svg>
    <div class="brand-name">Corvalt</div>
    <div class="contact-block">
      <p class="person-name">Mark Pell</p>
      <p class="role"><span class="title">Managing Director</span> <span class="company">Corvalt NZ Limited</span></p>
      <p class="contact-line">
        <svg viewBox="0 0 12 12"><rect x="0.5" y="2" width="11" height="8" fill="none" stroke="currentColor"/><path d="M0.5 2 L6 7 L11.5 2" fill="none" stroke="currentColor"/></svg>
        mark.pell@corvalt-example.co.nz
      </p>
      <p class="contact-line">
        <svg viewBox="0 0 12 12"><path d="M2 1 L4.5 1 L5 4 L3.5 5 Q4.8 7.5 7 8.5 L8 7 L11 7.5 L11 10 Q6 11 3 8 Q0.5 5 2 1 Z" fill="currentColor"/></svg>
        +64 027 604 91352
      </p>
    </div>
  </section>

  <section class="card card-back" aria-label="Card back">
    <div class="siren-glow" role="img" aria-label="Blurred photograph of red and blue emergency vehicle lights"></div>
    <div class="brand-name">Corvalt</div>
  </section>
</main>
</body>
</html>
```